タイトルは『集い準備応援戦団 ホール任せマン 集い段取り快勝手引きブック」とします。表紙、タイトルには戦隊もののヒーローを彷彿とさせるようなデザインを希望します。

ゴルフコンペの幹事業務がどんな内容なのかを細かく丁寧に説明し、尚且つ弊社のサービスがどんなメリットがあるのかを事細かに説明する内容です。サービスの概要を伝える見開き2ページの漫画と、詳細を記したデータを貼付します。

①表紙→②漫画→③詳細

このうち①、③を合わせてお願いしたいと思います。貼付内容の著作権は弊社にありますので、パンフレット内で画像等自由に使用してください。

ページ数に拘りはないのでわかりやすい内容にするために増えてしまっても問題ないです。

当方のコンセプトをよく理解し、さらに発展させてくれました。やりとりの中で当方の漠然としたイメージがどんどん具体化していき気持ちよかったです。最終的には12ページに渡る非常に素晴らしいものを納品していただきました。

確定が遅くなり申し訳ございませんでした。どれも素晴らしいご提案でした。また機会がありましたら宜しくお願い致します。

```html
<!DOCTYPE html>
<html lang="ja">
<head>
<meta charset="utf-8">
<title>集い段取り快勝手引きブック</title>
<link rel="stylesheet" href="https://fonts.googleapis.com/css2?family=Dela+Gothic+One&family=M+PLUS+1p:wght@700;800;900&display=swap">
<style>
  :root {
    --sun: #f7b81c;
    --sun-deep: #ec9a0e;
    --title-red: #d5141c;
    --ink: #2b1a10;
    --white: #ffffff;
    --maroon: #7a1a1c;
    --maroon-deep: #5a1012;
    --gold: #f3c21a;
    --field: #9aa23a;
    --field-dark: #5e6a22;
    --sky: #e9b63a;
  }
  * { box-sizing: border-box; margin: 0; padding: 0; }
  html, body { width: 848px; height: 1200px; overflow: hidden; background: #ffffff; }
  .cover {
    position: relative;
    width: 848px; height: 1200px;
    background: linear-gradient(180deg, var(--sun) 0%, var(--sun) 55%, var(--sun-deep) 100%);
    overflow: hidden;
    font-family: "M PLUS 1p", sans-serif;
  }
  .brand {
    position: absolute; top: 30px; left: 0; width: 100%;
    display: flex; flex-direction: column; align-items: center;
    color: var(--maroon);
  }
  .brand-row { display: flex; align-items: center; gap: 12px; }
  .brand-mark { width: 28px; height: 28px; background: var(--maroon); border-radius: 50%; }
  .brand-name { font-weight: 800; font-size: 36px; letter-spacing: 1px; }
  .brand-sub { font-weight: 700; font-size: 13px; margin-top: 2px; margin-left: 40px; }
  .title {
    position: absolute; top: 190px; left: 0; width: 100%;
    text-align: center;
    font-family: "Dela Gothic One", sans-serif;
    font-size: 78px; line-height: 1.3;
    color: var(--title-red);
    -webkit-text-stroke: 12px var(--white);
    paint-order: stroke fill;
    text-shadow: 4px 5px 0 rgba(60, 20, 0, 0.35);
  }
  .hero-art {
    position: absolute; top: 440px; left: 0; width: 100%; height: 500px;
    background:
      radial-gradient(ellipse 70% 55% at 50% 40%, rgba(255,255,255,0.15), transparent 70%),
      linear-gradient(180deg, var(--sky) 0%, var(--sky) 35%, var(--field) 60%, var(--field-dark) 100%);
  }
  .squad {
    position: absolute; top: 740px; left: 0; width: 100%;
    text-align: center;
  }
  .squad-unit {
    display: inline-block;
    font-weight: 900; font-size: 30px;
    color: var(--gold);
    -webkit-text-stroke: 6px var(--ink);
    paint-order: stroke fill;
    letter-spacing: 1px;
  }
  .squad-name {
    display: block; margin-top: 4px;
    font-family: "Dela Gothic One", sans-serif;
    font-size: 86px; line-height: 1.1;
    color: var(--title-red);
    -webkit-text-stroke: 10px var(--white);
    paint-order: stroke fill;
  }
  .service-band {
    position: absolute; top: 930px; left: 150px; width: 548px; height: 52px;
    background: var(--maroon);
    border: 4px solid var(--gold);
    display: flex; align-items: center; justify-content: center;
    color: var(--white); font-weight: 800; font-size: 27px; letter-spacing: 3px;
  }
  .foot-band {
    position: absolute; bottom: 0; left: 0; width: 100%; height: 90px;
    background: linear-gradient(180deg, var(--maroon) 0%, var(--maroon-deep) 100%);
    border-top: 4px solid var(--gold);
  }
</style>
</head>
<body>
  <main class="cover">
    <header class="brand">
      <div class="brand-row">
        <span class="brand-mark"></span>
        <span class="brand-name">HINODEDAI</span>
      </div>
      <span class="brand-sub">ひので台カントリークラブ</span>
    </header>

    <h1 class="title">集い段取り快勝<br>手引きブック</h1>

    <div class="hero-art" role="img" aria-label="ゴルフコースを背景に敬礼するスーツ姿の4人の幹事隊員のイラスト"></div>

    <div class="squad">
      <span class="squad-unit">集い準備応援戦団</span>
      <span class="squad-name">ホール任せマン</span>
    </div>

    <div class="service-band">ゴルフコンペ幹事業務代行サービス</div>

    <footer class="foot-band"></footer>
  </main>
</body>
</html>
```